Card design for Heating and Cooling company

this is for a heating and cooling company we recently updated our logo and need to update our cards. We attached our logo so you can incorporate it into the card. We specialize in residential and commercial furnace and air condition repairs. Have been in business since 2014.

Phone number 555.284.9137

We need the following phrases
:Repairs, Installations, and maintenance
:Quality work at reasonable prices
:residential/commercial
:Licensed &Insured
:Email Pinegrovehvac47@mailbox-example.com
Name: Teodor K (Ted)
Also on back side I would like my logo with wording :Thank you for your business and refferal

Industry/Entity Type

Hvac

Contact Information for Business Card

:residential/commercial
:Licensed & Insured
Name: Teodor K (Ted)
Number:555.284.9136

Requirements
Must have
• Blue and red colors
Nice to have
• Maybe a pic of a furnace or air conditioner

```html
<!DOCTYPE html>
<html lang="en">
<head>
<meta charset="utf-8">
<title>Pinegrove Heating &amp; Cooling – Business Card</title>
<link href="https://fonts.googleapis.com/css2?family=Montserrat:wght@400;500;600;700;800&display=swap" rel="stylesheet">
<style>
  :root {
    --page-bg: #e9e6e1;
    --card-white: #f7f7f7;
    --card-black: #141414;
    --ink: #1d1d1d;
    --ink-soft: #3a3a3a;
    --brand-red: #e5262b;
    --brand-orange: #f07a1f;
    --brand-blue: #45a8dc;
    --tick-blue: #2f8fd0;
    --unit-light: #d9d9d6;
    --unit-dark: #a9aaa6;
    --back-text: #d8d8d8;
  }
  * { box-sizing: border-box; margin: 0; padding: 0; }
  html, body {
    width: 1200px; height: 942px; overflow: hidden;
    background: var(--page-bg);
    font-family: "Montserrat", Arial, sans-serif;
  }
  .stage {
    width: 1200px; height: 942px;
    display: flex; align-items: center; justify-content: center; gap: 50px;
  }
  .card {
    width: 540px; height: 309px; position: relative; overflow: hidden;
    box-shadow: 0 10px 28px rgba(0,0,0,.25);
  }

  /* Front */
  .card-front { background: var(--card-white); color: var(--ink); }
  .color-band { position: absolute; top: 0; left: 0; width: 100%; height: 20px; }
  .card-front .details { position: absolute; left: 34px; top: 42px; width: 330px; }
  .person-name { font-size: 21px; font-weight: 600; letter-spacing: .5px; }
  .job-title { font-size: 12px; color: var(--brand-red); margin-top: 2px; font-family: Georgia, serif; }
  .contact { list-style: none; margin-top: 16px; font-size: 13px; color: var(--ink-soft); }
  .contact li { display: flex; align-items: center; gap: 8px; margin-bottom: 5px; }
  .contact svg { flex: none; }
  .services { list-style: none; margin-top: 20px; font-size: 13.5px; color: var(--ink); }
  .services li { display: flex; align-items: center; gap: 8px; margin-bottom: 4px; }
  .brand-front {
    position: absolute; right: 26px; top: 42px; width: 160px;
    display: flex; align-items: center; gap: 8px;
    font-size: 14px; font-weight: 700; color: var(--brand-blue); line-height: 1.15;
  }
  .brand-dot { width: 14px; height: 14px; border-radius: 50%; background: var(--brand-blue); flex: none; }
  .equipment-photo {
    position: absolute; right: 24px; bottom: 20px; width: 170px; height: 150px;
    background: linear-gradient(160deg, var(--unit-light), var(--unit-dark));
    border-radius: 4px;
  }

  /* Back */
  .card-back {
    background: radial-gradient(ellipse at 60% 30%, #2a2a2a, var(--card-black) 70%);
    display: flex; flex-direction: column; align-items: center; justify-content: center; gap: 34px;
  }
  .brand-back {
    display: flex; align-items: center; gap: 12px;
    font-size: 26px; font-weight: 700; color: #ffffff; letter-spacing: .5px;
  }
  .brand-back .brand-dot { width: 20px; height: 20px; }
  .thanks { font-size: 14px; color: var(--back-text); letter-spacing: .3px; }
</style>
</head>
<body>
<main class="stage">
  <section class="card card-front">
    <svg class="color-band" viewBox="0 0 540 20" preserveAspectRatio="none" aria-hidden="true">
      <defs>
        <linearGradient id="bandWarm" x1="0" x2="1">
          <stop offset="0" stop-color="#e5262b"/>
          <stop offset="1" stop-color="#f07a1f"/>
        </linearGradient>
      </defs>
      <polygon points="0,0 200,0 180,20 0,20" fill="url(#bandWarm)"/>
      <polygon points="200,0 540,0 540,8 193,8" fill="#45a8dc"/>
    </svg>

    <div class="details">
      <h1 class="person-name">TEODOR K (TED)</h1>
      <p class="job-title">Job Title</p>
      <ul class="contact">
        <li>
          <svg width="12" height="12" viewBox="0 0 12 12" aria-hidden="true"><rect width="12" height="12" rx="2" fill="#e5262b"/><path d="M3.5 3c1 0 1 1.5 1.5 2l-.6.6c.5 1 1.1 1.6 2 2l.6-.6c.5.5 2 .5 2 1.5 0 .8-.8 1.2-1.5 1.2C5 9.7 2.3 7 2.3 4.5 2.3 3.8 2.8 3 3.5 3z" fill="#fff"/></svg>
          555.284.9137
        </li>
        <li>
          <svg width="12" height="12" viewBox="0 0 12 12" aria-hidden="true"><rect width="12" height="12" rx="2" fill="#e5262b"/><path d="M3 3l6 6M9 3l-6 6" stroke="#fff" stroke-width="1.4"/></svg>
          Pinegrovehvac47@mailbox-example.com
        </li>
      </ul>
      <ul class="services">
        <li><svg width="13" height="13" viewBox="0 0 13 13" aria-hidden="true"><rect width="13" height="13" fill="#e8f2fa" stroke="#2f8fd0"/><path d="M3 6.5l2.5 2.5L10 3.5" stroke="#2f8fd0" stroke-width="2" fill="none"/></svg>Repairs, Installations, and maintenance</li>
        <li><svg width="13" height="13" viewBox="0 0 13 13" aria-hidden="true"><rect width="13" height="13" fill="#e8f2fa" stroke="#2f8fd0"/><path d="M3 6.5l2.5 2.5L10 3.5" stroke="#2f8fd0" stroke-width="2" fill="none"/></svg>Quality work at reasonable prices</li>
        <li><svg width="13" height="13" viewBox="0 0 13 13" aria-hidden="true"><rect width="13" height="13" fill="#e8f2fa" stroke="#2f8fd0"/><path d="M3 6.5l2.5 2.5L10 3.5" stroke="#2f8fd0" stroke-width="2" fill="none"/></svg>residential/commercial</li>
        <li><svg width="13" height="13" viewBox="0 0 13 13" aria-hidden="true"><rect width="13" height="13" fill="#e8f2fa" stroke="#2f8fd0"/><path d="M3 6.5l2.5 2.5L10 3.5" stroke="#2f8fd0" stroke-width="2" fill="none"/></svg>Licensed &amp;Insured</li>
      </ul>
    </div>

    <div class="brand-front"><span class="brand-dot"></span><span>Pinegrove Heating &amp; Cooling</span></div>
    <div class="equipment-photo" role="img" aria-label="Photo of a furnace and outdoor air conditioner unit"></div>
  </section>

  <section class="card card-back">
    <div class="brand-back"><span class="brand-dot"></span><span>Pinegrove Heating &amp; Cooling</span></div>
    <p class="thanks">Thank you for your business and refferal</p>
  </section>
</main>
</body>
</html>
```